Park Company Mobile Application Design

We are looking for deisgn of the mobile application for the parking company. More details about the parking company you can find on the following web site: www.lumrapark.mk.
As well we attached the parking card that this company is issuing. As you may see their preferred color is green.
Attached you can find screens that we are planning to implement in the mobile application.
If you need more details please contact us on dragan@kestrel.mk.

Thanks,
Dragan Petrusev
Kestrel Group

```html
<!DOCTYPE html>
<html lang="en">
<head>
<meta charset="utf-8">
<title>Lumra Park – Mobile App Screens</title>
<link rel="stylesheet" href="https://fonts.googleapis.com/css2?family=Open+Sans:wght@400;600;700&display=swap">
<style>
:root{
  --page:#283041;
  --map:#ededed;
  --green:#52b94a;
  --ink:#2f3746;
  --text:#3b3f47;
  --muted:#7a7f88;
  --field:#ffffff;
  --panel:#363d52;
  --desc:#c0c4cd;
  --nav-top:#4a5062;
  --nav-bottom:#252a36;
}
*{box-sizing:border-box;margin:0;padding:0}
html,body{width:911px;height:1200px;overflow:hidden;background:var(--page);font-family:"Open Sans",sans-serif;color:var(--text)}
.canvas{position:relative;width:911px;height:1200px}
.screen{position:absolute;width:280px;height:569px;overflow:hidden}
.map-bg{position:absolute;inset:0;background:radial-gradient(circle at 45% 30%,#e3e3e3 0,#efefef 45%,#f2f2f2 100%)}
.abs{position:absolute}
.brand{position:absolute;left:0;right:0;display:flex;align-items:center;justify-content:center;gap:8px;color:var(--green);font-weight:700;letter-spacing:.5px}
.brand .dot{border-radius:50%;background:var(--green);flex:none}
.brand-lg{top:196px;font-size:30px}
.brand-lg .dot{width:22px;height:22px}
.brand-md{top:36px;font-size:22px}
.brand-md .dot{width:16px;height:16px}
.brand-sm{top:22px;font-size:15px;gap:5px}
.brand-sm .dot{width:10px;height:10px}
.title{position:absolute;left:0;right:0;text-align:center;font-weight:700;font-size:23px;color:var(--ink);line-height:1}
.field{position:absolute;left:30px;width:219px;height:35px;background:var(--field);box-shadow:0 2px 5px rgba(0,0,0,.12);display:flex;align-items:center;padding:0 12px;font-size:11px;color:var(--muted);justify-content:space-between}
.field.filled{color:var(--text)}
.field svg{width:12px;height:12px;fill:#8a8e96}
.btn{position:absolute;height:35px;background:var(--green);color:#fff;font-weight:700;font-size:13px;display:flex;align-items:center;justify-content:center;letter-spacing:.3px}
.link{position:absolute;left:0;right:0;text-align:center;font-size:8.5px;color:var(--muted);text-decoration:underline}
.hint{position:absolute;left:0;right:0;text-align:center;font-size:11.5px}
.radio{position:absolute;left:76px;display:flex;align-items:center;gap:8px;font-size:16px;font-weight:600;color:var(--ink)}
.radio i{width:14px;height:14px;border:1.2px solid #555;border-radius:50%;display:flex;align-items:center;justify-content:center}
.radio i.on::after{content:"";width:7px;height:7px;border-radius:50%;background:var(--green)}
.round{position:absolute;top:21px;width:26px;height:26px;border:1.2px solid var(--ink);border-radius:50%;display:flex;align-items:center;justify-content:center;font-size:7.5px;font-weight:700;color:var(--ink)}
.round svg{width:12px;height:12px}
.menu{left:13px}.map-btn{left:240px}
.tabbar{position:absolute;left:13px;top:521px;width:253px;height:44px;display:flex;background:linear-gradient(var(--nav-top),var(--nav-bottom))}
.tab{flex:1;display:flex;flex-direction:column;align-items:center;justify-content:center;color:#fff;font-size:8px;line-height:1.1;text-align:center;border-right:1px solid #1d212b}
.tab:last-child{border-right:0}
.tab svg{width:13px;height:13px;fill:#fff;margin-bottom:2px}
.panel{position:absolute;left:13px;top:131px;width:253px;height:336px;background:var(--panel)}
.photo{position:absolute;left:9px;top:10px;width:113px;height:73px;background:radial-gradient(ellipse at 55% 55%,#5c5552 0,#7f7b78 40%,#a5a3a1 100%)}
.media-btn{position:absolute;left:131px;width:114px;height:35px;background:var(--green);color:#fff;font-size:11px;font-weight:600;display:flex;align-items:center;gap:8px;padding-left:10px}
.media-btn svg{width:16px;height:14px;fill:#fff}
.desc{position:absolute;left:9px;top:92px;width:236px;height:131px;background:var(--desc);padding:10px;font-size:11px;color:var(--text)}
.select{position:absolute;left:9px;top:237px;width:236px;height:35px;background:#fff;display:flex;align-items:center;justify-content:space-between;padding:0 12px;font-size:11px;color:var(--muted)}
.select svg{width:10px;height:10px;stroke:#777;fill:none;stroke-width:1.5}
</style>
</head>
<body>
<div class="canvas">

  <!-- Login -->
  <section class="screen" style="left:23px;top:23px">
    <div class="map-bg" role="img" aria-label="Faint city street map background"></div>
    <div class="brand brand-lg"><span class="dot"></span>Lumra Park</div>
    <div class="field" style="top:272px">Email Address</div>
    <div class="field" style="top:320px;letter-spacing:3px">********</div>
    <div class="link" style="top:372px">Forgot Password</div>
    <div class="btn" style="left:30px;top:399px;width:105px">REGISTER</div>
    <div class="btn" style="left:145px;top:399px;width:104px">LOG IN</div>
  </section>

  <!-- Forgot password -->
  <section class="screen" style="left:316px;top:23px">
    <div class="map-bg" role="img" aria-label="Faint city street map background"></div>
    <div class="brand brand-md"><span class="dot"></span>Lumra Park</div>
    <h1 class="title" style="top:141px">Forgot Password</h1>
    <div class="field filled" style="top:187px">petra.novak5@mailbox.mk</div>
    <p class="hint" style="top:241px">Send password reset code to the...</p>
    <div class="radio" style="top:272px"><i class="on"></i>Email address</div>
    <div class="radio" style="top:311px"><i></i>SMS to Mobile</div>
    <div class="btn" style="left:30px;top:349px;width:219px">SEND THE CODE</div>
    <div class="btn" style="left:30px;top:392px;width:219px">RESET THE PASSWORD</div>
  </section>

  <!-- Register -->
  <section class="screen" style="left:608px;top:23px">
    <div class="map-bg" role="img" aria-label="Faint city street map background"></div>
    <div class="brand brand-md"><span class="dot"></span>Lumra Park</div>
    <h1 class="title" style="top:144px">Identical Register</h1>
    <div class="field" style="top:188px">petra.novak4@mailbox.mk</div>
    <div class="field" style="top:236px">Password</div>
    <div class="field" style="top:284px">Confirm Password</div>
    <div class="field" style="top:332px">070555014</div>
    <div class="btn" style="left:88px;top:389px;width:105px">NEXT</div>
  </section>

  <!-- Pay parking -->
  <section class="screen" style="left:23px;top:605px">
    <div class="map-bg" role="img" aria-label="Faint city street map background"></div>
    <div class="round menu"><svg viewBox="0 0 12 12"><path d="M2 3h8M2 6h8M2 9h8" stroke="#2f3746" stroke-width="1.4"/></svg></div>
    <div class="brand brand-sm"><span class="dot"></span>Lumra Park</div>
    <div class="round map-btn">MAP</div>
    <h1 class="title" style="top:172px">Pay Parking</h1>
    <div class="field" style="top:211px">Parking zone<svg viewBox="0 0 12 12"><path d="M6 0a4 4 0 0 0-4 4c0 3 4 8 4 8s4-5 4-8a4 4 0 0 0-4-4zm0 5.6A1.6 1.6 0 1 1 6 2.4a1.6 1.6 0 0 1 0 3.2z"/></svg></div>
    <div class="field" style="top:259px">Duration of the parking in hours<svg viewBox="0 0 12 12"><circle cx="6" cy="6" r="5" fill="none" stroke="#8a8e96" stroke-width="1.3"/><path d="M6 3v3.3h2.3" fill="none" stroke="#8a8e96" stroke-width="1.3"/></svg></div>
    <div class="field" style="top:307px">License plate of the vehicle<svg viewBox="0 0 12 12"><path d="M2.5 5l1.2-3h4.6l1.2 3H11v4H10v1.5H8.5V9h-5v1.5H2V9H1V5zm1.2 0h4.6l-.7-2H4.4zM3 7.3a.8.8 0 1 0 0 .1zm6 0a.8.8 0 1 0 0 .1z"/></svg></div>
    <div class="btn" style="left:88px;top:360px;width:105px">PAY PARKING</div>
    <nav class="tabbar">
      <div class="tab"><svg viewBox="0 0 12 12"><path d="M2 6l1-3h5l1 3h1v3H9v1H8V9H3v1H2V9H1V6z"/></svg>PARKING<br>PLACES</div>
      <div class="tab"><svg viewBox="0 0 12 12"><path d="M1 4h9v6H1zM3 2h9v6h-1V3H3z"/></svg>PAY NOW</div>
      <div class="tab"><svg viewBox="0 0 12 12"><path d="M6 1l5.5 10h-11zM5.4 4.5v3.5h1.2V4.5zm0 4.5v1.2h1.2V9z" fill-rule="evenodd"/></svg>PARKING<br>ALERTS</div>
    </nav>
  </section>

  <!-- Report a problem -->
  <section class="screen" style="left:316px;top:605px">
    <div class="map-bg" role="img" aria-label="Faint city street map background"></div>
    <div class="round menu"><svg viewBox="0 0 12 12"><path d="M2 3h8M2 6h8M2 9h8" stroke="#2f3746" stroke-width="1.4"/></svg></div>
    <div class="brand brand-sm"><span class="dot"></span>Lumra Park</div>
    <div class="round map-btn">MAP</div>
    <h1 class="title" style="top:99px">Report a problem</h1>
    <div class="panel">
      <div class="photo" role="img" aria-label="Photo of a water-filled pothole in asphalt"></div>
      <div class="media-btn" style="top:10px"><svg viewBox="0 0 16 14"><path d="M5 1h6l1 2h3v10H1V3h3zm3 3.5a3 3 0 1 0 0 6 3 3 0 0 0 0-6z" fill-rule="evenodd"/></svg>Take a picture</div>
      <div class="media-btn" style="top:49px"><svg viewBox="0 0 16 14"><path d="M3 1h12v9H3zM4 2v7h10V2zm1 6l3-3 2 2 1.5-1.5L13 8zM1 3h1v9h11v1H1z" fill-rule="evenodd"/></svg>From Gallery</div>
      <div class="desc">Description of the problem</div>
      <div class="select">Category of the problem<svg viewBox="0 0 10 10"><path d="M1 3l4 4 4-4"/></svg></div>
      <div class="btn" style="left:75px;top:285px;width:105px">REPORT</div>
    </div>
    <nav class="tabbar">
      <div class="tab"><svg viewBox="0 0 12 12"><path d="M2 6l1-3h5l1 3h1v3H9v1H8V9H3v1H2V9H1V6z"/></svg>PARKING<br>PLACES</div>
      <div class="tab"><svg viewBox="0 0 12 12"><path d="M1 4h9v6H1zM3 2h9v6h-1V3H3z"/></svg>PAY NOW</div>
      <div class="tab"><svg viewBox="0 0 12 12"><path d="M6 1l5.5 10h-11zM5.4 4.5v3.5h1.2V4.5zm0 4.5v1.2h1.2V9z" fill-rule="evenodd"/></svg>PARKING<br>ALERTS</div>
    </nav>
  </section>

</div>
</body>
</html>
```